Wine Label for a Prosecco Wine Called Vuro

Prosecco is a white sparkling wine from Italy. We are looking for an eye catching, elegant label for this prosecco that is called "Vuro" because it is a young, fresh, lively white sparkling wine. (We do not want to see children or babies featured on the label-- just the name VURO please.) Attached is the old label for your reference, and the bottle type that will be used , which is a dark green Burgundy style bottle (pls ignore the label on the bottle). Please no grapes or wine glasses on the label. We are looking for something: eye catching / fun / ELEGANT (not cheap). We would be happy with a fun color too. Remember-- elegant, eye catching! Thanks!
Updates

Hi All, I think I made a mistake in my brief and have updated it. I also uploaded a competitor's label that we like very much to give better direction to what we are looking for. Also, the word Vuro cannot be vertical, nor can it be broken. It needs to read: VURO or Vuro. Thanks

Target Market(s)

American adults male and female.

Colors
abd036
33a6d7
33b8a4
ffcf3e

Requirements
Must have
• The mandatory information as shown on old labels. The word VURO should be very prominent.
Nice to have
• The uploaded photo of a competitor's prosecco shows a label we really like... if you could play around with this shape and style we'd be very happy.
Should not have
• No grape images, no wine glass images, no images of babies or children.

```html
<!DOCTYPE html>
<html lang="it">
<head>
<meta charset="utf-8">
<title>Vuro Prosecco – Wine Label</title>
<link rel="stylesheet" href="https://fonts.googleapis.com/css2?family=Cinzel:wght@400&family=Cormorant+Garamond:wght@500&family=Crimson+Text:ital@0;1&display=swap">
<style>
  :root {
    --page-bg: #f4f4f1;
    --label-green: #8dc63f;
    --label-green-deep: #72b534;
    --label-ink: #ffffff;
  }

  * { box-sizing: border-box; margin: 0; padding: 0; }

  html, body {
    width: 1200px;
    height: 860px;
    overflow: hidden;
    background: var(--page-bg);
  }

  .canvas {
    position: relative;
    width: 1200px;
    height: 860px;
  }

  .wine-label {
    position: absolute;
    left: 317px;
    top: 70px;
    width: 566px;
    height: 720px;
    background: var(--label-green);
    border-radius: 0 42px 0 54px;
    overflow: hidden;
    color: var(--label-ink);
    text-align: center;
  }

  .ornament-area {
    position: absolute;
    display: block;
  }

  .ornament-area--top-right {
    right: 0;
    top: 0;
    width: 230px;
    height: 180px;
    background: radial-gradient(ellipse at 80% 20%, var(--label-green-deep) 0%, rgba(114,181,52,0.55) 45%, rgba(141,198,63,0) 75%);
  }

  .ornament-area--left {
    left: 0;
    top: 330px;
    width: 190px;
    height: 390px;
    background: radial-gradient(ellipse at 15% 70%, var(--label-green-deep) 0%, rgba(114,181,52,0.5) 45%, rgba(141,198,63,0) 75%);
  }

  .label-content {
    position: absolute;
    inset: 0;
  }

  .brand-name {
    position: absolute;
    left: 0;
    right: 0;
    top: 168px;
    font-family: "Cinzel", serif;
    font-weight: 400;
    font-size: 168px;
    line-height: 1;
    letter-spacing: 0.01em;
  }

  .wine-type {
    position: absolute;
    left: 30px;
    right: 54px;
    top: 348px;
    display: flex;
    align-items: center;
    gap: 18px;
  }

  .wine-type__rule {
    flex: 1;
    height: 2px;
    background: var(--label-ink);
  }

  .wine-type__name {
    font-family: "Cormorant Garamond", serif;
    font-weight: 500;
    font-size: 40px;
    line-height: 1;
    letter-spacing: 0.2em;
    margin-right: -0.2em;
  }

  .appellation {
    position: absolute;
    left: 0;
    right: 20px;
    top: 412px;
    font-family: "Crimson Text", serif;
    font-style: italic;
    font-size: 29px;
    line-height: 1;
  }

  .region {
    position: absolute;
    left: 0;
    right: 20px;
    top: 446px;
    font-family: "Crimson Text", serif;
    font-size: 32px;
    line-height: 1;
    letter-spacing: 0.12em;
  }

  .style-note {
    position: absolute;
    left: 0;
    right: 24px;
    top: 612px;
    font-family: "Cormorant Garamond", serif;
    font-weight: 500;
    font-size: 25px;
    line-height: 1;
    letter-spacing: 0.2em;
  }
</style>
</head>
<body>
  <main class="canvas">
    <section class="wine-label">
      <div class="ornament-area ornament-area--top-right" role="img" aria-label="Tone-on-tone green scroll ornament in the top right corner"></div>
      <div class="ornament-area ornament-area--left" role="img" aria-label="Tone-on-tone green scroll ornament along the lower left edge"></div>

      <div class="label-content">
        <h1 class="brand-name">Vuro</h1>
        <div class="wine-type">
          <span class="wine-type__rule"></span>
          <span class="wine-type__name">PROSECCO</span>
          <span class="wine-type__rule"></span>
        </div>
        <p class="appellation">Indicazione Geografica Tipica</p>
        <p class="region">Veneto</p>
        <p class="style-note">FRIZZANTE</p>
      </div>
    </section>
  </main>
</body>
</html>
```